Carrowell Business Card Re-design

Our current cards are outdated. This is our website www.carrowellinsights.example. We would like something that is "on-brand" and consistent with our social media sites. We are strategic consultants with a core competency in Marketing Research. Although, please know we are considering a brand logo redesign and potentially a new look. If we like your work here we will invite you to participate when we get to that project. Thank you very much. Harriet
Here are our social sites: https://twitter.com/Carrowell?lang=en
https://plus.google.com/+Carrowellinsights
https://www.linkedin.com/company/5094827/
https://www.facebook.com/CarrowellInc/
Business

```html
<!DOCTYPE html>
<html lang="en">
<head>
<meta charset="utf-8">
<title>Carrowell Business Card</title>
<link rel="stylesheet" href="https://fonts.googleapis.com/css2?family=Work+Sans:wght@400;500;600&display=swap">
<style>
  :root {
    --green: #5cbd3a;
    --ink: #2a2a2a;
    --muted: #555;
    --paper: #ffffff;
    --stage: #3a3a3c;
    --night-1: #0f1a2e;
    --night-2: #1d3446;
    --night-3: #2f4a52;
  }
  * { box-sizing: border-box; margin: 0; padding: 0; }
  html, body { width: 1200px; height: 900px; overflow: hidden; }
  body {
    background: var(--stage);
    font-family: "Work Sans", Arial, sans-serif;
    position: relative;
  }
  .card {
    position: absolute;
    left: 290px;
    width: 620px;
    height: 354px;
    overflow: hidden;
    box-shadow: 0 10px 26px rgba(0,0,0,.45);
  }
  /* back of card */
  .card--back { top: 70px; }
  .card__photo {
    position: absolute; inset: 0;
    background:
      radial-gradient(ellipse at 70% 35%, rgba(90,130,150,.45), transparent 60%),
      linear-gradient(135deg, var(--night-1) 0%, var(--night-2) 55%, var(--night-3) 100%);
  }
  .card--back .brand {
    position: absolute; left: 0; right: 0; top: 120px;
    text-align: center;
    font-size: 64px; font-weight: 600; letter-spacing: 2px;
    color: var(--green);
    text-transform: lowercase;
  }
  .social-row {
    position: absolute; left: 0; right: 0; top: 250px;
    display: flex; justify-content: center; gap: 14px;
  }
  .social-row span {
    width: 22px; height: 22px; border-radius: 50%;
    background: #d8dde2;
    border: 2px solid var(--green);
  }
  /* front of card */
  .card--front { top: 470px; background: var(--paper); }
  .person { position: absolute; left: 30px; top: 26px; }
  .person__name {
    color: var(--green); font-weight: 500; font-size: 21px;
    text-transform: uppercase; letter-spacing: .3px;
  }
  .person__role { color: var(--muted); font-size: 13px; margin-top: 2px; }
  .card--front .brand {
    position: absolute; right: 44px; top: 140px;
    font-size: 48px; font-weight: 600; letter-spacing: 2px;
    color: var(--green); text-transform: lowercase;
  }
  .contact {
    position: absolute; left: 30px; top: 232px;
    list-style: none; font-size: 15px; color: var(--ink);
  }
  .contact li { display: flex; align-items: center; gap: 10px; line-height: 23px; }
  .contact svg { width: 11px; height: 11px; flex: none; }
  .contact .accent { color: var(--green); }
  .address {
    position: absolute; right: 30px; top: 266px;
    text-align: right; font-size: 17px; line-height: 24px; color: var(--ink);
  }
  .band {
    position: absolute; left: 0; right: 0; bottom: 0; height: 12px;
    background: var(--green);
  }
</style>
</head>
<body>

<section class="card card--back">
  <div class="card__photo" role="img" aria-label="Dark blue photograph of hands on a keyboard with a glowing network of connected profile circles"></div>
  <div class="brand">carrowell</div>
  <div class="social-row" aria-label="Social media links">
    <span></span><span></span><span></span><span></span>
    <span></span><span></span><span></span><span></span>
  </div>
</section>

<section class="card card--front">
  <div class="person">
    <div class="person__name">Dorian Felsted</div>
    <div class="person__role">Director</div>
  </div>

  <div class="brand">carrowell</div>

  <ul class="contact">
    <li>
      <svg viewBox="0 0 12 12"><path d="M3 1 L5 3.5 L4 5 Q5 7 7 8 L8.5 7 L11 9 L9.5 11 Q4 10.5 1 3 Z" fill="var(--green)"/></svg>
      407.555.0187
    </li>
    <li>
      <svg viewBox="0 0 12 12"><rect x="1" y="2.5" width="10" height="7" fill="none" stroke="var(--green)" stroke-width="1.2"/><path d="M1 2.5 L6 6.5 L11 2.5" fill="none" stroke="var(--green)" stroke-width="1.2"/></svg>
      info@carrowellinsights.example
    </li>
    <li>
      <svg viewBox="0 0 12 12"><circle cx="6" cy="6" r="5" fill="none" stroke="var(--green)" stroke-width="1.2"/><path d="M1 6 H11 M6 1 Q3 6 6 11 M6 1 Q9 6 6 11" fill="none" stroke="var(--green)" stroke-width="1"/></svg>
      <span>www.<span class="accent">carrowellinsights</span>.example</span>
    </li>
  </ul>

  <address class="address" style="font-style:normal">
    14 Harcourt Lane<br>
    London, England, N4 2QS
  </address>

  <div class="band"></div>
</section>

</body>
</html>
```